Tavi Academy

I need different posters for a high school that displays positive messaging and the school's core values.
Want the design to look sleek for high school aged children

1. Poster #1
CORE VALUES:
• RESPECT
• RESPONSIBILITY
• LEADERSHIP
• PRIDE
• COMMUNITY

2. Acronym posters for the school
Empathy
Zeal
Respect
Aspire

3. additional acronym poster
Encourage
Zenith
Relationships
Accountability

```html
<!DOCTYPE html>
<html lang="en">
<head>
<meta charset="utf-8">
<title>Tavi Academy – Core Values Posters</title>
<link rel="stylesheet" href="https://fonts.googleapis.com/css2?family=Roboto+Condensed:wght@700&display=swap">
<style>
  :root {
    --canvas-bg: #f6f6f6;
    --poster-bg: #e7e7e9;
    --header-blue: #17679a;
    --text-white: #ffffff;
    --orange: #ee8a22;
    --pink: #ec0c86;
    --green: #8dc140;
    --red: #ec1c26;
    --yellow: #f7e000;
  }
  * { box-sizing: border-box; margin: 0; padding: 0; }
  html, body {
    width: 1200px; height: 680px; overflow: hidden;
    background: var(--canvas-bg);
    font-family: "Roboto Condensed", "Arial Narrow", sans-serif;
  }
  .canvas { position: relative; width: 1200px; height: 680px; }
  .poster {
    position: absolute; top: 101px; width: 337px; height: 477px;
    background: var(--poster-bg);
    box-shadow: 0 2px 5px rgba(0,0,0,0.25);
  }
  .poster--values { left: 78px; }
  .poster--acronym { left: 431px; }
  .poster--extra { left: 785px; }
  .poster__header {
    height: 80px; background: var(--header-blue);
    display: flex; align-items: center; justify-content: center;
    color: var(--text-white); font-size: 44px; font-weight: 700;
    padding-top: 4px; white-space: nowrap;
  }
  .value-band {
    position: absolute; left: 34px; width: 266px;
    display: flex; align-items: center; justify-content: center;
    color: var(--text-white); font-weight: 700; white-space: nowrap;
    box-shadow: -2px 2px 0 rgba(255,255,255,0.9);
  }
  .poster--values .value-band { height: 56px; font-size: 32px; }
  .poster--acronym .value-band,
  .poster--extra .value-band { left: 35px; height: 66px; font-size: 33px; }
  .value-band--orange { background: var(--orange); }
  .value-band--pink { background: var(--pink); }
  .value-band--green { background: var(--green); }
  .value-band--red { background: var(--red); }
  .value-band--yellow { background: var(--yellow); }
</style>
</head>
<body>
<main class="canvas">
  <section class="poster poster--values">
    <h2 class="poster__header">CORE VALUES</h2>
    <div class="value-band value-band--orange" style="top:104px">RESPECT</div>
    <div class="value-band value-band--pink" style="top:181px">RESPONSIBILITY</div>
    <div class="value-band value-band--green" style="top:255px">LEADERSHIP</div>
    <div class="value-band value-band--red" style="top:333px">PRIDE</div>
    <div class="value-band value-band--yellow" style="top:404px">COMMUNITY</div>
  </section>

  <section class="poster poster--acronym">
    <h2 class="poster__header">ACRONYM</h2>
    <div class="value-band value-band--orange" style="top:106px">EMPATHY</div>
    <div class="value-band value-band--pink" style="top:196px">ZEAL</div>
    <div class="value-band value-band--green" style="top:286px">RESPECT</div>
    <div class="value-band value-band--red" style="top:376px">ASPIRE</div>
  </section>

  <section class="poster poster--extra">
    <h2 class="poster__header">ADD. ACRONYM</h2>
    <div class="value-band value-band--orange" style="top:106px">ENCOURAGE</div>
    <div class="value-band value-band--pink" style="top:196px">ZENITH</div>
    <div class="value-band value-band--green" style="top:286px">RELATIONSHIPS</div>
    <div class="value-band value-band--red" style="top:376px">ACCOUNTABILITY</div>
  </section>
</main>
</body>
</html>
```